Graphics Design of Physics Book

Hi
Size : 8" x 11.25"
We are education book Publication Company and would like to have book cover for "Physics" it has 4 volumes. All 4 having the same color scheme and design except the volume no.
Blue is my personal favorite but u can use any color. Want to have a band at the bottom of the cover to place our Logo “VARNEL Education” a PDF of the same is attached, or you can place logo anywhere according to ur design.
I need “Physics” as title of the book to be visible prominently.
And volume and volume no. should also be Visible and eye catching I prefer a Graphic to enhance the Volume No.
A background pattern can also be a option (it should be vector form so that color can be change later)
Please do not offer any cut and paste design I need very professional presentation.
Volume and Number can be in metallic 3D (CMYK) effect.
only Professional presentation will get feedback.
I have provided a sample artwork for reference do not follow it but can be a reference what I needed !

Target Market(s)

Students Class 9th to 12th

Industry/Entity Type

Education

Font styles to use
Serif

Colors
3176b5
0555a3
85abd2
cadf82
abd036
9bcb3c

Requirements
Must have
• Eye catching.
• “Physics” as title of the book to be visible prominently.
• volume and volume no. should also be Visible and eye catching
• I prefer a Graphic to enhance the Volume No.
• Icons for
• 1. Questions and answers
• 2. Theory Notes
• 3. Tips & Tricks
• 4. Previous Year's Reference Questions
• 5. Covers Complete Syllabus
Nice to have
• decent seamless background or metallic 3d effect (not to be print in special Ink) design should only be in CMYK.
Should not have
• Physics related Pictures or Icons (Specially E=mc2) or any scientist photograph or I Need pure graphic design

```html
<!DOCTYPE html>
<html lang="en">
<head>
<meta charset="utf-8">
<title>Physics Volume 1 – Book Cover</title>
<link rel="stylesheet" href="https://fonts.googleapis.com/css2?family=Open+Sans:ital,wght@0,600;0,800;1,600&family=Oswald:wght@700&display=swap">
<style>
  :root {
    --page-bg: #eef0f3;
    --cover-blue: #1fa3e4;
    --cover-blue-deep: #0a78c4;
    --cover-blue-light: #5cc3f2;
    --band-dark: #0b0e14;
    --ink-blue: #1457a8;
    --swoosh-grey: #b9bec6;
    --paper: #ffffff;
    --metal-hi: #ffffff;
    --metal-mid: #c9ced6;
    --metal-low: #7d848f;
  }
  * { box-sizing: border-box; margin: 0; padding: 0; }
  html, body { width: 1200px; height: 976px; overflow: hidden; }
  body {
    background: var(--page-bg);
    font-family: "Open Sans", Arial, sans-serif;
    position: relative;
  }
  .cover {
    position: absolute;
    top: 98px;
    width: 555px;
    height: 780px;
    overflow: hidden;
    box-shadow: 0 10px 30px rgba(0,0,0,.18);
  }
  .cover--back { left: 30px; background: var(--paper); }
  .cover--front { left: 615px; background: var(--cover-blue); }
  .cover-art { position: absolute; inset: 0; width: 100%; height: 100%; }

  /* back cover features */
  .feature-list {
    position: absolute;
    top: 150px;
    left: 40px;
    list-style: none;
  }
  .feature {
    display: flex;
    align-items: center;
    gap: 18px;
    height: 74px;
    color: var(--ink-blue);
    font-style: italic;
    font-weight: 600;
    font-size: 21px;
  }
  .feature-icon { width: 46px; height: 46px; flex: none; }

  /* imprint band */
  .imprint {
    position: absolute;
    left: 40px;
    bottom: 26px;
    display: flex;
    align-items: center;
    gap: 8px;
    font-weight: 800;
    font-size: 15px;
    letter-spacing: .5px;
    color: var(--ink-blue);
  }
  .imprint-mark { width: 12px; height: 12px; background: var(--ink-blue); }
  .cover--front .imprint { color: var(--paper); }
  .cover--front .imprint-mark { background: var(--paper); }

  /* front cover type */
  .book-title {
    position: absolute;
    top: 46px;
    right: 34px;
    font-weight: 800;
    font-size: 74px;
    letter-spacing: 3px;
    color: var(--paper);
    text-shadow: 0 3px 0 #0a5f9e, 0 6px 10px rgba(0,0,0,.35);
  }
  .volume-label {
    position: absolute;
    left: 40px;
    top: 540px;
    font-family: "Oswald", Impact, sans-serif;
    font-weight: 700;
    font-size: 96px;
    letter-spacing: 2px;
    line-height: 1;
    background: linear-gradient(180deg, var(--metal-hi) 0%, var(--metal-mid) 45%, var(--metal-low) 52%, var(--metal-hi) 100%);
    -webkit-background-clip: text;
    background-clip: text;
    color: transparent;
    filter: drop-shadow(0 4px 3px rgba(0,0,0,.45));
  }
</style>
</head>
<body>

  <!-- Back cover -->
  <section class="cover cover--back">
    <svg class="cover-art" viewBox="0 0 555 780" aria-hidden="true">
      <defs>
        <linearGradient id="backBand" x1="0" y1="0" x2="1" y2="1">
          <stop offset="0" stop-color="#5cc3f2"/>
          <stop offset="1" stop-color="#0a78c4"/>
        </linearGradient>
      </defs>
      <path d="M0 0 H555 V118 C420 150 300 30 170 40 C90 46 40 60 0 72 Z" fill="url(#backBand)"/>
      <path d="M0 86 C60 70 110 58 180 56 C310 50 420 168 555 140" fill="none" stroke="#b9bec6" stroke-width="5"/>
      <rect x="0" y="750" width="555" height="30" fill="#1fa3e4"/>
    </svg>

    <ul class="feature-list">
      <li class="feature">
        <svg class="feature-icon" viewBox="0 0 46 46" aria-hidden="true">
          <ellipse cx="23" cy="19" rx="19" ry="15" fill="#1457a8"/>
          <path d="M12 30 L8 42 L22 33 Z" fill="#1457a8"/>
          <text x="23" y="27" text-anchor="middle" font-family="Open Sans, sans-serif" font-weight="800" font-size="22" fill="#fff">?</text>
        </svg>
        Questions and answers
      </li>
      <li class="feature">
        <svg class="feature-icon" viewBox="0 0 46 46" aria-hidden="true">
          <rect x="6" y="4" width="34" height="38" fill="#fff" stroke="#1457a8" stroke-width="2"/>
          <path d="M11 14 H35 M11 20 H35 M11 26 H35 M11 32 H28" stroke="#1457a8" stroke-width="1.6"/>
        </svg>
        Theory Notes
      </li>
      <li class="feature">
        <svg class="feature-icon" viewBox="0 0 46 46" aria-hidden="true">
          <rect x="7" y="6" width="32" height="36" rx="4" fill="#fff" stroke="#1457a8" stroke-width="3"/>
          <rect x="16" y="2" width="14" height="8" rx="2" fill="#1457a8"/>
          <path d="M13 20 l3 3 l5 -6 M13 31 l3 3 l5 -6 M25 20 H34 M25 31 H34" fill="none" stroke="#1457a8" stroke-width="2"/>
        </svg>
        Tips &amp; Tricks
      </li>
      <li class="feature">
        <svg class="feature-icon" viewBox="0 0 46 46" aria-hidden="true">
          <path d="M16 10 L30 23 L16 36" fill="none" stroke="#9aa0a8" stroke-width="5"/>
        </svg>
        Previous Year's Reference Questions
      </li>
      <li class="feature">
        <svg class="feature-icon" viewBox="0 0 46 46" aria-hidden="true">
          <path d="M16 10 L30 23 L16 36" fill="none" stroke="#9aa0a8" stroke-width="5"/>
        </svg>
        Complete Syllabus
      </li>
    </ul>

    <div class="imprint"><span class="imprint-mark"></span>VARNEL Education</div>
  </section>

  <!-- Front cover -->
  <section class="cover cover--front">
    <svg class="cover-art" viewBox="0 0 555 780">
      <defs>
        <linearGradient id="frontBlue" x1="0" y1="0" x2="0" y2="1">
          <stop offset="0" stop-color="#1fa3e4"/>
          <stop offset=".5" stop-color="#2bb0ee"/>
          <stop offset="1" stop-color="#1494d8"/>
        </linearGradient>
        <radialGradient id="artGlow" cx=".45" cy=".5" r=".6">
          <stop offset="0" stop-color="#e2652a"/>
          <stop offset=".35" stop-color="#7a3b6e"/>
          <stop offset=".7" stop-color="#1c2a3a"/>
          <stop offset="1" stop-color="#0b0e14"/>
        </radialGradient>
      </defs>
      <rect width="555" height="780" fill="url(#frontBlue)" aria-hidden="true"/>
      <path d="M0 230 C120 150 250 180 360 240 C440 282 500 300 555 290 V520 C480 540 420 520 320 470 C200 410 110 400 0 440 Z"
            fill="#ffffff" aria-hidden="true"/>
      <path d="M0 240 C120 162 250 192 360 252 C440 294 500 312 555 302 V506 C480 526 420 506 320 456 C200 398 110 388 0 428 Z"
            fill="url(#artGlow)" role="img" aria-label="Abstract glowing streams of coloured light and particles on a dark background"/>
    </svg>

    <h1 class="book-title">PHYSICS</h1>
    <div class="volume-label">VOLUME - 1</div>
    <div class="imprint"><span class="imprint-mark"></span>VARNEL Education</div>
  </section>

</body>
</html>
```